LOGO DESIGN: Construction Related Service Business

We require a logo for our business Dovtar Services. We are a construction related business offering a range of services including machine services for groundworks (digging trenches, soak wells, preparing land for construction etc), demolition and truck haulage from demolition sites.
We would like our logo to be predominately text, but may include abstract graphics. The colour scheme should be mainly a mid bright blue and overall be quite 'clean'.

Industry/Entity Type

Construction

Contact Information for Business Card

Colin Pruett
Ph:041 562 9083
dovtarservices@keloran.com.au

Colors
0456a3

```html
<!DOCTYPE html>
<html lang="en">
<head>
<meta charset="utf-8">
<title>Dovtar Services – Business Card Options</title>
<link rel="stylesheet" href="https://fonts.googleapis.com/css2?family=Arimo:wght@400;700&display=swap">
<style>
  :root {
    --brand-blue: #2558a2;
    --brand-green: #8dc63f;
    --card-white: #ffffff;
    --ink: #333333;
    --ink-soft: #555555;
    --backdrop: #9a9a98;
    --label: #c4c4c2;
    --divider-light: #cfcfcf;
  }
  * { box-sizing: border-box; margin: 0; padding: 0; }
  html, body {
    width: 1200px;
    height: 610px;
    overflow: hidden;
    background: var(--backdrop);
    font-family: "Arimo", Arial, sans-serif;
  }
  .board {
    display: flex;
    width: 1200px;
    height: 610px;
  }
  .option {
    position: relative;
    width: 600px;
    height: 610px;
    display: flex;
    flex-direction: column;
    align-items: center;
    justify-content: center;
    gap: 28px;
  }
  .option + .option { border-left: 2px solid #b5b5b3; }
  .option-label {
    position: absolute;
    top: 22px;
    left: 24px;
    font-size: 32px;
    font-weight: 700;
    color: var(--label);
  }
  .card {
    width: 330px;
    height: 188px;
    border-radius: 2px;
    box-shadow: 0 3px 10px rgba(0,0,0,0.25);
  }
  .card--white { background: var(--card-white); color: var(--ink); }
  .card--blue { background: var(--brand-blue); color: var(--card-white); }

  /* Option A: mark on the left, details on the right */
  .card-split {
    display: flex;
    align-items: center;
    padding: 0 26px;
  }
  .brand-stack {
    width: 104px;
    display: flex;
    flex-direction: column;
    align-items: flex-start;
    gap: 6px;
  }
  .brand-square {
    width: 48px;
    height: 48px;
    background: var(--brand-green);
  }
  .brand-stack .brand-name {
    font-size: 14px;
    font-weight: 700;
    line-height: 1.1;
  }
  .card--white .brand-name { color: var(--brand-blue); }
  .card--blue .brand-name { color: var(--card-white); }
  .split-divider {
    width: 1px;
    height: 96px;
    margin: 0 18px 0 4px;
  }
  .card--white .split-divider { background: var(--divider-light); }
  .card--blue .split-divider { background: var(--brand-green); }
  .details { display: flex; flex-direction: column; gap: 5px; font-size: 9px; }
  .person { font-size: 11px; margin-bottom: 8px; }
  .person strong { font-weight: 700; }
  .card--blue .person { color: var(--brand-green); }

  /* Option B: centred wordmark */
  .card-centred {
    display: flex;
    flex-direction: column;
    align-items: center;
    justify-content: center;
    gap: 12px;
  }
  .brand-line {
    display: flex;
    align-items: center;
    gap: 8px;
  }
  .brand-dot {
    width: 14px;
    height: 14px;
    border-radius: 50%;
  }
  .card--white .brand-dot { background: var(--brand-blue); }
  .card--blue .brand-dot { background: var(--card-white); }
  .brand-line .brand-name { font-size: 26px; font-weight: 400; }
  .card-centred .person { margin: 0; }
  .contact-row { font-size: 9px; }
  .card--white .contact-row { color: var(--ink-soft); }
</style>
</head>
<body>
<main class="board">

  <section class="option option--a">
    <h2 class="option-label">Option A</h2>

    <article class="card card--white card-split">
      <div class="brand-stack">
        <span class="brand-square"></span>
        <span class="brand-name">Dovtar Services</span>
      </div>
      <span class="split-divider"></span>
      <div class="details">
        <p class="person">Colin <strong>Pruett</strong></p>
        <p>P : 041 562 9083</p>
        <p>E : dovtarservices@keloran.com.au</p>
      </div>
    </article>

    <article class="card card--blue card-split">
      <div class="brand-stack">
        <span class="brand-square"></span>
        <span class="brand-name">Dovtar Services</span>
      </div>
      <span class="split-divider"></span>
      <div class="details">
        <p class="person">Colin <strong>Pruett</strong></p>
        <p>P : 041 562 9083</p>
        <p>E : dovtarservices@keloran.com.au</p>
      </div>
    </article>
  </section>

  <section class="option option--b">
    <h2 class="option-label">Option B</h2>

    <article class="card card--white card-centred">
      <div class="brand-line">
        <span class="brand-dot"></span>
        <span class="brand-name">Dovtar Services</span>
      </div>
      <p class="person">Colin <strong>Pruett</strong></p>
      <p class="contact-row">P : 041 562 9083 &nbsp;|&nbsp; E : dovtarservices@keloran.com.au</p>
    </article>

    <article class="card card--blue card-centred">
      <div class="brand-line">
        <span class="brand-dot"></span>
        <span class="brand-name">Dovtar Services</span>
      </div>
      <p class="person">Colin <strong>Pruett</strong></p>
      <p class="contact-row">P : 041 562 9083 &nbsp;|&nbsp; E : dovtarservices@keloran.com.au</p>
    </article>
  </section>

</main>
</body>
</html>
```